Anzeigengestaltung für KFZ-Werkstatt
Zielgruppe
Wir sind eine KFZ-Werkstatt mit vielumfänglichen Dienstleistungen. Unsere Zielgruppe beschränkt sich auf einen Umkreis von ca. 10km. Wir bieten alles rund ums KFZ: Service, Inspektion, Reparaturen aller Art, TÜV, Rad/Reifen/Felgen, Spurvermessung, Unfallinstandsetzung.
Aufgabenstellung
wir nutzen den Hashtag '#wagenhofmoosl' für Werbung im Internet sowie in den Werbeanzeigen. Wir verwenden diesen 'Slogan' in der SChriftart 'Hashtag', diese kann überall runtergeladen werden. dieser muss in den Werbeanzeigen nicht im Vordergrund stehen, da hier die Zielgruppe eher in Richtung 40+ geht.
es muss auch Platz für die offizielle Firmierung samt Anschrift, Telefon und Internet sein (kein Fax).
was die Anzeige an sich angeht, so sollte das Motiv (gerne erst mal einfach ein Stockfoto) durch uns austauschbar sein. Sprich: wenn Reifensaison ist, wollen wir da ein eigenes Motiv reinstecken können; im Sommer wiederum ein anderes etc. Zudem verwenden wir auch Standardfotos von unserem Unternehmen, welches wir platzieren lassen wenn ein Monat mal nichts besonderes ansteht (die Werbung wird monatlich geschaltet).
Maße: 172x100mm
Hauptfarben (bedingt durch das System, an das wir angeschlossen sind):
ROT: C15 M100 Y100 K0 (oder HKS15; oder Pantone 1797)
GRAU: C0 M0 Y0 K50 (oder 50% HKS90; oder Pantone Cool Gray 7)
Aufgrund der Zielgruppe haben wir als Wunsch 'erschwinglich' angegeben. Dies soll aber nicht heißen, dass wir nicht bereit sind, für das Erstellen der Anzeige kein Geld auszugeben. Nein, damit wollen wir unterstreichen, dass es nicht irre aufgepusht sein soll mit wahnsinns-Effekten etc.

```html
<!DOCTYPE html>
<html lang="de">
<head>
<meta charset="utf-8">
<title>Anzeige Werkstatt</title>
<link rel="stylesheet" href="https://fonts.googleapis.com/css2?family=Caveat:wght@500&family=Outfit:wght@400;500&display=swap">
<style>
  :root{
    --stage:#262626;
    --brand-red:#d2232a;
    --photo-deep:#a31a1f;
    --photo-mid:#c21f25;
    --band-grey:#9a9a9e;
    --ink:#111111;
    --white:#ffffff;
    --badge-blue:#0a5fb0;
    --badge-light:#f2f2f2;
  }
  *{margin:0;padding:0;box-sizing:border-box}
  html,body{width:1200px;height:1200px;overflow:hidden;background:var(--stage)}
  .ad{position:absolute;left:112px;top:317px;width:975px;height:567px;background:var(--brand-red);overflow:hidden}
  .motif{position:absolute;left:512px;top:0;width:463px;height:470px;
    background:radial-gradient(ellipse at 62% 45%,var(--photo-mid) 0%,var(--photo-deep) 60%,var(--brand-red) 100%)}
  .hashtag{position:absolute;left:50px;top:44px;font-family:"Caveat",cursive;font-weight:500;font-size:100px;color:var(--white);line-height:1;letter-spacing:-1px}
  .services{position:absolute;left:97px;top:180px;list-style:none;font-family:"Outfit",sans-serif;font-weight:500;font-size:26px;letter-spacing:0.6px;color:var(--white)}
  .services li{height:36px;line-height:36px;position:relative;padding-left:34px}
  .services li::before{content:"";position:absolute;left:0;top:15px;width:7px;height:7px;border-radius:50%;background:var(--white)}
  .badge{position:absolute}
  .badge-one{left:571px;top:351px;width:94px;height:94px;border-radius:50%;background:var(--badge-light)}
  .badge-two{left:683px;top:315px;width:87px;height:130px;border-radius:6px;background:var(--badge-blue)}
  .badge-three{left:787px;top:352px;width:122px;height:94px;border-radius:6px;background:var(--white)}
  .contact-band{position:absolute;left:0;top:470px;width:975px;height:97px;background:var(--band-grey);font-family:"Outfit",sans-serif;font-weight:500;font-size:26px;color:var(--ink);letter-spacing:0.6px}
  .contact-band span,.contact-band svg{position:absolute}
  .contact-band span{top:31px}
  .address{left:39px}
  .phone-icon{left:368px;top:25px}
  .phone{left:420px}
  .mail-icon{left:606px;top:32px}
  .email{left:654px;font-weight:400}
</style>
</head>
<body>
<section class="ad">
  <div class="motif" role="img" aria-label="Foto eines lächelnden Mechanikers in Arbeitsjacke, rot eingefärbt"></div>
  <div class="hashtag">#wagenhofmoosl</div>
  <ul class="services">
    <li>SERVICE</li>
    <li>INSPEKTION</li>
    <li>REPARATUREN ALLER ART</li>
    <li>TÜV</li>
    <li>RAD/REIFEN/FELGEN</li>
    <li>SPURVERMESSUNG</li>
    <li>UNFALLINSTANDSETZUNG</li>
  </ul>
  <div class="badge badge-one" role="img" aria-label="Platz für Prüfsiegel"></div>
  <div class="badge badge-two" role="img" aria-label="Platz für Meisterbetrieb-Siegel"></div>
  <div class="badge badge-three" role="img" aria-label="Platz für Auszeichnung"></div>
  <footer class="contact-band">
    <span class="address">LINDENWEG 17</span>
    <svg class="phone-icon" width="44" height="44" viewBox="0 0 44 44" aria-hidden="true">
      <circle cx="22" cy="22" r="22" fill="var(--ink)"/>
      <path d="M27 11 l5 4 q1 1 0 2 l-3 3 q-4 -1 -7 6 q-2 5 1 7 l-2 3 q-1 1 -2 0 l-3 -3 q-3 -8 3 -15 q4 -6 8 -7 z" fill="var(--white)"/>
    </svg>
    <span class="phone">09471-3820</span>
    <svg class="mail-icon" width="39" height="30" viewBox="0 0 39 30" aria-hidden="true">
      <rect x="0" y="0" width="39" height="30" rx="2" fill="var(--ink)"/>
      <path d="M2 3 L19.5 17 L37 3 M2 27 L14 14 M37 27 L25 14" fill="none" stroke="var(--band-grey)" stroke-width="2"/>
    </svg>
    <span class="email">info@wagenhofmoosl.de</span>
  </footer>
</section>
</body>
</html>
```